Physician focused educational website needed

We are looking to create a fresh, simple website to help Physicians understand the benefits of protecting their largest asset....their income. We are wanting to create a site that can be a resource to help answer the FAQ that physicians ask regarding Disability Insurance. The goal is not to sell DI but rather to education the physician on the importance of the product and to be a resource for them to learn more.

Target Market(s)

Physicians

Industry/Entity Type

Insurance

Coding

Coded - Design and coding required

Number of Pages Required

1 page

Requirements
Must have
• easy to navigate and understand FAQ format

```html
<!DOCTYPE html>
<html lang="en">
<head>
<meta charset="utf-8">
<title>Steadfast Cover – Frequently Asked Questions</title>
<link href="https://fonts.googleapis.com/css2?family=Mulish:wght@400;600;700&display=swap" rel="stylesheet">
<style>
:root{
  --green:#8bc34a;
  --blue:#1fa6ef;
  --ink:#333333;
  --muted:#555555;
  --line:#e4e4e4;
  --footer:#1b1b1b;
  --footer-text:#a9a9a9;
  --white:#ffffff;
}
*{margin:0;padding:0;box-sizing:border-box}
html,body{width:913px;height:1200px;overflow:hidden;background:var(--white)}
body{font-family:"Mulish",sans-serif;color:var(--ink);position:relative}
.abs{position:absolute}

/* header */
.site-header{position:absolute;left:0;top:0;width:913px;height:48px;border-bottom:1px solid #d8d8d8;background:var(--white)}
.brand{left:61px;top:17px;font-family:"Mulish",sans-serif;font-size:10.5px;font-weight:700;letter-spacing:.4px;color:#333}
.nav a{position:absolute;top:17px;font-size:9.5px;color:#333;text-decoration:none}
.share{left:746px;top:17px}
.menu{left:886px;top:17px}

/* title band */
.title-band{left:0;top:48px;width:913px;height:63px;background:var(--green)}
.title-band h1{position:absolute;left:71px;top:18px;font-size:21px;font-weight:400;color:var(--white);letter-spacing:.5px}
.crumbs{left:71px;top:125px;font-size:10.5px;color:#555;display:flex;align-items:center;gap:6px}
.crumbs .sep{color:#bbb}
.rule{left:0;top:152px;width:913px;height:1px;background:var(--line)}

/* faq */
.section-title{position:absolute;left:71px;font-size:17px;font-weight:400;color:#222}
.faq-item{position:absolute;left:71px;width:470px;font-size:12px;line-height:19px;color:#444}
.faq-item .toggle{display:inline-block;width:26px;height:26px;background:var(--blue);vertical-align:middle;margin-right:10px;position:relative;top:-2px}
.faq-item .toggle::before,.faq-item .toggle::after{content:"";position:absolute;background:var(--white);left:50%;top:50%;transform:translate(-50%,-50%)}
.faq-item .toggle::before{width:12px;height:2px}
.faq-item .toggle::after{width:2px;height:12px}

/* sidebar */
.topics{left:599px;top:207px;width:243px;border:1px solid var(--green)}
.topics li{list-style:none;height:29px;line-height:29px;padding-left:10px;font-size:10.5px;color:var(--green);border-top:1px solid var(--green)}
.topics li:first-child{border-top:none}
.side-title{position:absolute;left:599px;font-size:16px;font-weight:400;color:#222}
.side-list{position:absolute;left:599px;list-style:none}
.side-list li{height:25px;font-size:10.5px;color:var(--green);display:flex;align-items:center;gap:7px}
.doc{width:9px;height:11px;border:1px solid #999;border-radius:1px;position:relative;flex:none}
.doc::after{content:"";position:absolute;left:1.5px;top:3px;width:4px;height:4px;border-top:1px solid #999;border-bottom:1px solid #999}

/* footer */
.site-footer{position:absolute;left:0;top:910px;width:913px;height:290px;background:var(--footer)}
.foot-title{position:absolute;top:54px;font-size:11px;font-weight:600;color:var(--white)}
.foot-list{position:absolute;top:78px;list-style:none}
.foot-list li{height:24px;font-size:9.5px;color:var(--footer-text);display:flex;align-items:center;gap:7px}
.foot-list .doc{border-color:#888}
.foot-list .doc::after{border-color:#888}
.foot-text{position:absolute;font-size:9.5px;line-height:20.3px;color:var(--footer-text)}
.socials{position:absolute;top:232px;left:382px;display:flex;gap:10px}
.socials span{width:10px;height:10px;border-radius:50%;background:#bdbdbd}
.copyright{position:absolute;top:261px;width:913px;text-align:center;font-size:8px;color:#aaa}
</style>
</head>
<body>

<header class="site-header">
  <div class="abs brand">STEADFAST COVER</div>
  <nav class="nav">
    <a style="left:437px">Disability Insurance</a>
    <a style="left:545px">Guidelines</a>
    <a style="left:611px">Faq</a>
    <a style="left:648px">Contact Us</a>
    <a style="left:791px">Blog</a>
  </nav>
  <svg class="abs share" width="11" height="12" viewBox="0 0 11 12" aria-label="Share">
    <circle cx="9" cy="2" r="1.8" fill="#333"/><circle cx="2" cy="6" r="1.8" fill="#333"/><circle cx="9" cy="10" r="1.8" fill="#333"/>
    <path d="M9 2 L2 6 L9 10" stroke="#333" stroke-width="1" fill="none"/>
  </svg>
  <svg class="abs menu" width="15" height="12" viewBox="0 0 15 12" aria-label="Menu">
    <rect y="0" width="15" height="2" fill="#222"/><rect y="5" width="15" height="2" fill="#222"/><rect y="10" width="15" height="2" fill="#222"/>
  </svg>
</header>

<div class="abs title-band"><h1>Frequently Asked Questions</h1></div>
<div class="abs crumbs">
  <svg width="11" height="10" viewBox="0 0 11 10" aria-label="Home"><path d="M1 5 L5.5 1 L10 5 M2.5 4 V9 H8.5 V4" stroke="var(--green)" stroke-width="1.1" fill="none"/></svg>
  <span class="sep">/</span><span>FAQ</span>
</div>
<div class="abs rule"></div>

<main>
  <h2 class="section-title" style="top:205px">Section A</h2>
  <p class="faq-item" style="top:248px"><span class="toggle"></span>When is the right time to buy Income Protection plan/should I buy while in training/Is there an advantage to buying as a PGY 1?</p>
  <p class="faq-item" style="top:308px"><span class="toggle"></span>Wouldn’t my group coverage cover me adequately? (what is the difference between group/private)</p>
  <p class="faq-item" style="top:368px"><span class="toggle"></span>What features should I look for?</p>
  <p class="faq-item" style="top:414px"><span class="toggle"></span>What is true own occupation/specialty specific mean?</p>

  <h2 class="section-title" style="top:490px">Section B</h2>
  <p class="faq-item" style="top:534px"><span class="toggle"></span>What is Catestrophic Benefit?</p>
  <p class="faq-item" style="top:580px"><span class="toggle"></span>What is DIRS? (disability income retirement supplement)</p>
  <p class="faq-item" style="top:627px"><span class="toggle"></span>What if my health changes after I buy coverage?</p>
  <p class="faq-item" style="top:674px"><span class="toggle"></span>Can I raise my coverage after I enter practice?</p>

  <h2 class="section-title" style="top:750px">Section C</h2>
  <p class="faq-item" style="top:794px"><span class="toggle"></span>What is inflation protection? (COLA)</p>
  <p class="faq-item" style="top:840px"><span class="toggle"></span>Can they raise my rates or cancel me in the future? What if I move, will my discount still apply?</p>
</main>

<aside>
  <ul class="abs topics">
    <li>Getting Started</li><li>Coverage</li><li>Benefits</li><li>Guide</li><li>Troubleshooting</li><li>Video Tutorials</li>
  </ul>
  <h3 class="side-title" style="top:415px">Recent Blog</h3>
  <ul class="side-list" style="top:442px">
    <li><i class="doc"></i>Lorem ipsum dolor</li>
    <li><i class="doc"></i>Lorem ipsum dolor sit amet</li>
    <li><i class="doc"></i>Lorem ipsum dolor</li>
    <li><i class="doc"></i>Lorem ipsum dolor sit amet</li>
  </ul>
  <h3 class="side-title" style="top:569px">Popular Articles</h3>
  <ul class="side-list" style="top:597px">
    <li><i class="doc"></i>Lorem ipsum dolor sit amet</li>
    <li><i class="doc"></i>Lorem ipsum dolor</li>
    <li><i class="doc"></i>Lorem ipsum dolor sit amet</li>
    <li><i class="doc"></i>Lorem ipsum dolor</li>
  </ul>
</aside>

<footer class="site-footer">
  <h4 class="foot-title" style="left:71px">Popular Articles</h4>
  <ul class="foot-list" style="left:71px">
    <li><i class="doc"></i>Lorem ipsum dolor sit amet</li>
    <li><i class="doc"></i>Lorem ipsum dolor</li>
    <li><i class="doc"></i>Lorem ipsum dolor sit amet</li>
    <li><i class="doc"></i>Lorem ipsum dolor</li>
  </ul>
  <h4 class="foot-title" style="left:269px">Recent Blogs</h4>
  <ul class="foot-list" style="left:269px">
    <li><i class="doc"></i>Lorem ipsum dolor</li>
    <li><i class="doc"></i>Lorem ipsum dolor sit amet</li>
    <li><i class="doc"></i>Lorem ipsum dolor</li>
    <li><i class="doc"></i>Lorem ipsum dolor sit amet</li>
  </ul>
  <h4 class="foot-title" style="left:466px">Latest Tweets</h4>
  <p class="foot-text" style="left:466px;top:79px;width:170px">
    › Lorem ipsum dolor sit amet, consectetur adipiscing elit, sed do… @lark http://larkfieldstudio.net<br>
    › Lorem ipsum dolor sit amet, consectetur adipiscing elit, sed do… @lark http://larkfieldstudio.net
  </p>
  <h4 class="foot-title" style="left:665px">Address</h4>
  <p class="foot-text" style="left:665px;top:79px;width:155px">27 Orchard Lane, Near Riverside Market, Millbrook, Eastland 560112</p>
  <h4 class="foot-title" style="left:665px;top:162px">Email ID</h4>
  <p class="foot-text" style="left:665px;top:180px">hello@larkfieldstudio.net</p>
  <div class="socials" aria-label="Social links"><span></span><span></span><span></span><span></span><span></span><span></span><span></span><span></span></div>
  <p class="copyright">© 2016 Build By Larkfield Studio</p>
</footer>

</body>
</html>
```